Criação de Kit com 5 Layouts de Post para Redes Sociais (Facebook, Instagram e etc) para Artes, Música & Entretenimento
" Será um canal onde ocorre jogos de RPG, Games e talvez podcast "

```html
<!DOCTYPE html>
<html lang="pt-BR">
<head>
<meta charset="UTF-8">
<title>A Panelada – Agenda</title>
<link rel="stylesheet" href="https://fonts.googleapis.com/css2?family=Open+Sans:wght@700;800&display=swap">
<style>
  :root {
    --bg-light: #fff1cc;
    --bg-warm: #fde2a6;
    --orange-top: #f9b25a;
    --orange-bottom: #ef8a2f;
    --red-band: #d8331d;
    --brand: #d8331d;
    --white: #ffffff;
    --photo-a: #c9a58a;
    --photo-b: #6f5a4d;
  }
  * { margin: 0; padding: 0; box-sizing: border-box; }
  html, body { width: 1200px; height: 1200px; overflow: hidden; }
  body { font-family: "Open Sans", Arial, sans-serif; }

  .post {
    position: relative;
    width: 1200px;
    height: 1200px;
    background: radial-gradient(circle at 50% 45%, var(--bg-light) 0%, var(--bg-warm) 100%);
  }

  .brand {
    position: absolute;
    top: 95px;
    left: 0;
    width: 1200px;
    display: flex;
    justify-content: center;
    align-items: center;
    gap: 22px;
  }
  .brand-dot {
    width: 54px; height: 54px;
    border-radius: 50%;
    background: var(--brand);
  }
  .brand-name {
    font-weight: 800;
    font-size: 70px;
    color: var(--brand);
    letter-spacing: 1px;
    text-transform: uppercase;
  }

  .portrait {
    position: absolute;
    border-radius: 50%;
    border: 8px solid var(--white);
    background: linear-gradient(160deg, var(--photo-a), var(--photo-b));
    box-shadow: 0 4px 14px rgba(120, 70, 20, 0.18);
  }

  .band {
    position: absolute;
    display: flex;
    align-items: center;
    justify-content: center;
    color: var(--white);
    font-weight: 700;
    white-space: nowrap;
  }
  .band-name {
    height: 72px;
    font-size: 40px;
    background: linear-gradient(180deg, var(--orange-top), var(--orange-bottom));
    clip-path: polygon(4% 0, 100% 0, 97% 100%, 0 100%);
  }
  .band-date {
    height: 70px;
    font-size: 30px;
    background: var(--red-band);
    clip-path: polygon(3% 0, 100% 0, 96% 100%, 0 100%);
  }
</style>
</head>
<body>
  <main class="post">
    <header class="brand">
      <span class="brand-dot"></span>
      <span class="brand-name">A Panelada</span>
    </header>

    <!-- Linha 1 -->
    <div class="portrait" role="img" aria-label="Foto de retrato do participante 1" style="left:106px; top:322px; width:220px; height:220px;"></div>
    <div class="band band-name" style="left:360px; top:343px; width:492px;">NOME SOBRENOME</div>
    <div class="band band-date" style="left:336px; top:413px; width:492px;">DIA 00 ÀS 21:00HS</div>

    <!-- Linha 2 -->
    <div class="portrait" role="img" aria-label="Foto de retrato do participante 2" style="left:864px; top:480px; width:240px; height:240px;"></div>
    <div class="band band-name" style="left:343px; top:547px; width:509px;">NOME SOBRENOME</div>
    <div class="band band-date" style="left:365px; top:619px; width:499px;">DIA 00 ÀS 21:00HS</div>

    <!-- Linha 3 -->
    <div class="portrait" role="img" aria-label="Foto de retrato do participante 3" style="left:86px; top:679px; width:250px; height:250px;"></div>
    <div class="band band-name" style="left:360px; top:754px; width:485px;">NOME SOBRENOME</div>
    <div class="band band-date" style="left:336px; top:824px; width:492px;">DIA 00 ÀS 21:00HS</div>

    <!-- Linha 4 -->
    <div class="portrait" role="img" aria-label="Foto de retrato do participante 4" style="left:869px; top:888px; width:240px; height:240px;"></div>
    <div class="band band-name" style="left:343px; top:960px; width:509px;">NOME SOBRENOME</div>
    <div class="band band-date" style="left:365px; top:1032px; width:499px;">DIA 00 ÀS 21:00HS</div>
  </main>
</body>
</html>
```